New Velbrix Business Card Design

We need a business card to match our new branding. The look should utilize the elements as attached here (Vector files & new exec overview are attached.) I really like 'organic' looking elements (e.g. an idea would be to have this printed on recycled paper stock). Thank you! Looking forward to seeing your designs.

Business

```html
<!DOCTYPE html>
<html lang="en">
<head>
<meta charset="utf-8">
<title>Velbrix Business Card</title>
<link href="https://fonts.googleapis.com/css2?family=Exo+2:wght@400;700&display=swap" rel="stylesheet">
<style>
  :root {
    --page: #e9e6e1;
    --brand-blue: #1677c4;
    --strip-blue: #2a86d0;
    --rule-navy: #2c4ba8;
    --logo-blue: #1b6fbf;
    --leaf-green: #6cbd45;
    --paper: #ffffff;
    --ink: #1c1c1c;
  }
  * { margin: 0; padding: 0; box-sizing: border-box; }
  html, body { width: 1200px; height: 1050px; overflow: hidden; }
  body {
    background: var(--page);
    font-family: "Exo 2", sans-serif;
    position: relative;
  }
  .card {
    position: absolute;
    left: 320px; top: 125px;
    width: 560px; height: 800px;
    background: var(--brand-blue);
    overflow: hidden;
    box-shadow: 0 10px 30px rgba(0,0,0,0.18);
  }
  .card-head {
    position: absolute; left: 0; top: 0; width: 100%; height: 212px;
    background: var(--paper);
    border-top: 14px solid var(--strip-blue);
    border-bottom: 12px solid var(--rule-navy);
  }
  .brand {
    position: absolute; left: 240px; top: 66px;
    display: flex; align-items: center; gap: 14px;
  }
  .brand-dot {
    width: 26px; height: 26px; border-radius: 50%;
    background: var(--leaf-green);
  }
  .brand-name {
    font-size: 64px; font-weight: 400; color: var(--logo-blue);
    letter-spacing: 1px; line-height: 1;
  }
  .connectors { position: absolute; left: 0; top: 0; }
  .name-plate {
    position: absolute; left: 210px; top: 180px;
    width: 330px; height: 105px;
    background: var(--paper);
    text-align: center; padding-top: 14px;
  }
  .person-name {
    font-size: 38px; font-weight: 700; color: var(--leaf-green);
    letter-spacing: 1px; line-height: 1.1;
  }
  .person-role { font-size: 22px; color: var(--ink); margin-top: 4px; }
  .contact-box {
    position: absolute; left: 150px;
    width: 350px; height: 100px;
    border: 3px solid var(--paper);
    color: var(--paper); text-align: center;
    padding-top: 16px;
  }
  .contact-label { font-size: 26px; font-weight: 700; letter-spacing: 1px; }
  .contact-value { font-size: 21px; margin-top: 4px; letter-spacing: 1px; }
  .contact-phone { top: 320px; }
  .contact-email { top: 450px; }
  .contact-web { top: 580px; }
  .accent-rule {
    position: absolute; left: 0; top: 706px; width: 100%; height: 5px;
    background: var(--leaf-green);
  }
  .address {
    position: absolute; left: 0; top: 730px; width: 100%;
    text-align: center; color: var(--paper);
    font-size: 25px; letter-spacing: 1.5px;
  }
</style>
</head>
<body>
  <article class="card">
    <header class="card-head">
      <div class="brand">
        <span class="brand-dot"></span>
        <span class="brand-name">Velbrix</span>
      </div>
    </header>

    <svg class="connectors" width="560" height="800" viewBox="0 0 560 800" aria-hidden="true">
      <g stroke="#ffffff" stroke-width="3" fill="none">
        <line x1="50" y1="240" x2="50" y2="630"/>
        <line x1="50" y1="240" x2="210" y2="240"/>
        <line x1="50" y1="370" x2="150" y2="370"/>
        <line x1="50" y1="500" x2="150" y2="500"/>
        <line x1="50" y1="630" x2="150" y2="630"/>
      </g>
    </svg>

    <div class="name-plate">
      <p class="person-name">DANIEL OKAFOR</p>
      <p class="person-role">Managing Director</p>
    </div>

    <div class="contact-box contact-phone">
      <p class="contact-label">PHONE</p>
      <p class="contact-value">014 552 7830</p>
    </div>
    <div class="contact-box contact-email">
      <p class="contact-label">EMAIL</p>
      <p class="contact-value">hello@velbrixmail.com</p>
    </div>
    <div class="contact-box contact-web">
      <p class="contact-label">WEBSITE</p>
      <p class="contact-value">www.velbrixstudio.com</p>
    </div>

    <div class="accent-rule"></div>
    <p class="address">071.12th floor,Harbor Crest Road NTV</p>
  </article>
</body>
</html>
```